Business Card for beauty technology startup

Design Glowmi Business Card for a Beauty, based on the website identity and colors (https://www.glowmi-example.com).
Glowmi is a beauty tech startup that gathers helpful product info for beauty lovers and consumers (such as availability on stores, price range and product reviews) for makeup products. The card design must be young, colorful but clean, and very modern.

Target Market(s)

woman, 15-35

Industry/Entity Type

Cosmetics

Contact Information for Business Card

Full Name, address, phone

Font styles to use
Other font styles liked:
• Advent Pro

Colors
e34297
86cfc6
ffffff
5c5c5c
e8e8e8
e667a6
b2b2b2

Requirements
Must have
• One full colored side with a creative design and another with card info
• Use Color palette: #95C5C5 and/or #D38AA5
• Use fonts: Advent Pro
• Use website identity: https://www.glowmi-example.com
Nice to have
• If needed extra font: Roboto

```html
<!DOCTYPE html>
<html lang="en">
<head>
<meta charset="utf-8">
<title>Glowmi Business Card</title>
<link rel="stylesheet" href="https://fonts.googleapis.com/css2?family=Josefin+Sans:wght@300&family=Montserrat:wght@400;600&display=swap">
<style>
  :root {
    --teal: #93c2c0;
    --plum: #4a3440;
    --rose: #c0708f;
    --ink: #3e3e3e;
    --paper: #ffffff;
    --table: #d4d4d4;
  }
  * { margin: 0; padding: 0; box-sizing: border-box; }
  html, body { width: 1200px; height: 800px; overflow: hidden; }
  body {
    background: var(--table);
    display: flex;
    align-items: center;
    justify-content: center;
    gap: 40px;
  }
  .card {
    position: relative;
    width: 525px;
    height: 300px;
    overflow: hidden;
    box-shadow: 0 4px 14px rgba(0,0,0,.12);
  }
  .card--front {
    background: var(--teal);
    display: flex;
    align-items: center;
    justify-content: center;
  }
  .brand-mark {
    display: flex;
    align-items: center;
    gap: 14px;
  }
  .brand-dot {
    width: 26px; height: 26px;
    border: 3px solid var(--paper);
    border-radius: 50%;
  }
  .brand-name {
    font-family: "Josefin Sans", sans-serif;
    font-weight: 300;
    letter-spacing: 8px;
    text-transform: uppercase;
    white-space: nowrap;
  }
  .card--front .brand-name { color: var(--paper); font-size: 52px; }

  .card--back { background: var(--paper); }
  .card--back svg.swoosh { position: absolute; inset: 0; }
  .social {
    position: absolute;
    top: 18px; left: 340px;
    display: flex; gap: 8px;
  }
  .social span {
    width: 14px; height: 14px;
    border-radius: 50%;
    background: var(--paper);
    box-shadow: 0 0 0 1px var(--plum);
  }
  .back-mark {
    position: absolute;
    top: 46px; left: 385px;
    display: flex; align-items: center; gap: 8px;
  }
  .back-mark .brand-dot { width: 18px; height: 18px; border: 2px solid var(--plum); background: var(--paper); }
  .back-mark .brand-name { color: var(--plum); font-size: 18px; letter-spacing: 3px; }
  .card--back .wordmark {
    position: absolute;
    right: 34px; top: 150px;
    color: var(--plum);
    font-size: 50px;
    letter-spacing: 6px;
  }
  .contact {
    position: absolute;
    left: 36px; bottom: 28px;
    font-family: "Montserrat", sans-serif;
    color: var(--ink);
    font-size: 12px;
    line-height: 1.45;
  }
  .contact .person { color: var(--rose); font-weight: 600; font-size: 17px; letter-spacing: .5px; text-transform: uppercase; }
  .contact .role { font-size: 9px; letter-spacing: 1px; text-transform: uppercase; margin-bottom: 6px; }
  .contact ul { list-style: none; margin-top: 4px; }
  .contact li { display: flex; align-items: center; gap: 10px; }
  .contact li svg { width: 10px; height: 10px; flex: none; }
</style>
</head>
<body>
  <section class="card card--front" aria-label="Card front">
    <div class="brand-mark">
      <span class="brand-dot"></span>
      <span class="brand-name">Glowmi</span>
    </div>
  </section>

  <section class="card card--back" aria-label="Card back">
    <svg class="swoosh" viewBox="0 0 525 300" width="525" height="300" aria-hidden="true">
      <path d="M0 0 H525 V30 C470 58 410 80 330 88 C220 100 90 84 0 20 Z" fill="var(--teal)"/>
      <path d="M0 30 C90 95 220 112 330 100 C410 92 470 70 525 40"
            fill="none" stroke="var(--plum)" stroke-width="5"/>
    </svg>
    <div class="social" aria-hidden="true"><span></span><span></span><span></span><span></span></div>
    <div class="back-mark">
      <span class="brand-dot"></span>
      <span class="brand-name">Glowmi</span>
    </div>
    <div class="brand-name wordmark">Glowmi</div>
    <div class="contact">
      <div class="person">Lena Morrow</div>
      <div class="role">Owner</div>
      <div>48 Palm Crest Way</div>
      <div>Seabrook, FL 33000</div>
      <ul>
        <li><svg viewBox="0 0 10 10"><path d="M2 1 L4 1 L4.5 3 L3.3 4 Q4.5 6 6 6.8 L7 5.5 L9 6 L9 8 Q5 9 1.5 4.5 Q1 2.5 2 1Z" fill="var(--rose)"/></svg>555.014.2290</li>
        <li><svg viewBox="0 0 10 10"><rect x=".8" y="2" width="8.4" height="6" fill="none" stroke="var(--rose)"/><path d="M1 2.3 L5 5.5 L9 2.3" fill="none" stroke="var(--rose)"/></svg>info@glowmi-example.com</li>
        <li><svg viewBox="0 0 10 10"><circle cx="5" cy="5" r="4" fill="none" stroke="var(--rose)"/><path d="M1 5 H9 M5 1 V9" stroke="var(--rose)" stroke-width=".8"/></svg>www.glowmi-example.com</li>
      </ul>
    </div>
  </section>
</body>
</html>
```